Gigwharf.com contest! Design our Homepage!

Gigwharf.com is looking for the world's best Graphic Designer!

If you have what it takes to mold pixels in a way that creates a show stopping, eye popping, OMGWOW-factor design, then we want you!

Over the next couple of weeks we'll be running a few design contests to find out which of you has what it takes to be deemed our very own Gigwharf.com Graphic Design Elite.

This is your chance to re-imagine the look and feel of your favorite outsourcing website! The winner will not only win the cash prize for the contest, but will be also considered for future work on Gigwharf.com projects.

Your mission for this contest:
- We want you to redesign our very own homepage (www.gigwharf.com).
- Ensure you keep all functionality intact in your design (feel free to include the current header and footer in your design or create your own)
- Enter as many design ideas as you want - the winner will be selected by the end of the contest deadline.

It's that simple...

You're still here? The clock is ticking! Get creative and submit your design ideas today!

```html
<!DOCTYPE html>
<html lang="en">
<head>
<meta charset="utf-8">
<title>Gigwharf.com – Homepage</title>
<link rel="stylesheet" href="https://fonts.googleapis.com/css2?family=Open+Sans:ital,wght@0,300;0,400;0,600;0,700;1,400&family=Oswald:wght@300;400;500&display=swap">
<style>
:root{
  --ink:#0b1e22;
  --ink-2:#0f2a2e;
  --band:#163a3d;
  --teal:#4db3b3;
  --sky:#29a3dc;
  --lime:#a6c93a;
  --orange:#f0892a;
  --paper:#f6f7f7;
  --grey:#dcdddd;
  --white:#ffffff;
  --text:#222;
  --muted:#6f7b7d;
}
*{margin:0;padding:0;box-sizing:border-box}
html,body{width:1200px;height:3479px;overflow:hidden}
body{position:relative;font-family:'Open Sans',sans-serif;color:var(--text);background:var(--white)}
.abs{position:absolute}

/* header */
.site-header{position:absolute;left:0;top:0;width:1200px;height:125px;background:var(--ink)}
.brand{position:absolute;left:36px;top:44px;display:flex;align-items:center;gap:12px;color:var(--sky);font-weight:700;font-size:30px}
.brand i{width:26px;height:26px;background:var(--sky);display:block}
.main-nav{position:absolute;left:334px;top:62px;display:flex;gap:31px;font-size:14px;color:var(--white);font-weight:600}
.main-nav a:nth-child(4){margin-right:-13px}
.login{position:absolute;left:1030px;top:20px;width:54px;height:18px;background:#3a5a98;border-radius:2px;color:#fff;font-size:9px;text-align:center;line-height:18px}
.account{position:absolute;left:1103px;top:21px;font-size:12px;color:#c8d0d2}
.search{position:absolute;left:924px;top:56px;width:264px;height:34px;background:#1c2f33;border:1px solid #2d4246;color:#c3cbcd;font-size:12px;font-style:italic;padding:8px 24px}

/* hero */
.hero{position:absolute;left:0;top:125px;width:1200px;height:461px;background:radial-gradient(ellipse at 70% 40%,#2b9d9f 0%,#1d7073 45%,#16494d 100%)}
.hero h1{position:absolute;left:70px;top:70px;font-weight:300;font-size:46px;line-height:57px;color:#fff}
.hero h1 b{font-weight:700}
.hero .lead{position:absolute;left:74px;top:208px;font-size:15px;color:#e8f2f2}
.sel{position:absolute;left:74px;top:247px;width:210px;height:50px;border-radius:25px;background:var(--teal);color:#fff;font-size:19px;padding:11px 37px}
.sel:after{content:"";position:absolute;right:26px;top:21px;border:7px solid transparent;border-top:9px solid #fff}
.hero-btn{position:absolute;left:303px;top:247px;width:210px;height:50px;border-radius:25px;background:var(--ink);color:#fff;font-size:19px;text-align:center;line-height:50px}
.hero hr{position:absolute;left:72px;top:324px;width:490px;border:0;border-top:1px solid rgba(255,255,255,.25)}
.hero .about{position:absolute;left:71px;top:340px;width:500px;font-size:13px;line-height:23px;color:#fff}
.map{position:absolute;left:600px;top:60px;width:560px;height:275px;border-radius:40px;background:radial-gradient(ellipse,#30b8ea 0%,#20a6dc 55%,rgba(32,166,220,0) 75%)}
.hero .count{position:absolute;left:686px;top:360px;font-size:17px;color:#fff}

/* how it works */
.section-title{position:absolute;width:1200px;text-align:center;font-family:'Oswald',sans-serif;font-weight:400;font-size:52px;letter-spacing:-1px;color:#111}
.section-title span{color:var(--teal)}
.how span{color:var(--sky)}
.steps-art{position:absolute;left:60px;top:760px;width:440px;height:400px;border-radius:50%;background:radial-gradient(ellipse,rgba(166,201,58,.55) 0%,rgba(77,179,179,.35) 45%,rgba(255,255,255,0) 72%)}
.tooltip{position:absolute;left:48px;top:818px;width:144px;height:110px;background:#333a3c;border-radius:6px;color:#fff;font-size:17px;line-height:22px;text-align:center;padding-top:22px}
.video{position:absolute;left:651px;top:770px;width:440px;height:250px;background:linear-gradient(135deg,#f4f6f8 0%,#bfe2f4 50%,#eef1f4 100%);border:1px solid #ccd}
.video .bar{position:absolute;left:0;bottom:0;width:100%;height:22px;background:#111}
.video .bar i{position:absolute;left:0;top:0;width:185px;height:3px;background:#d12}
.pill{position:absolute;border-radius:10px;font-family:'Oswald',sans-serif;font-weight:300;text-align:center;color:#fff}
.post-free{left:649px;top:1066px;width:440px;height:76px;background:var(--teal);font-size:32px;line-height:76px;box-shadow:0 4px 6px rgba(0,0,0,.2)}
.post-free b{font-weight:400;color:var(--ink)}
.stat-line{position:absolute;font-family:'Oswald',sans-serif;font-weight:300;font-size:32px;color:#fff}
.stat-line b{font-weight:400;color:#1f74b4}

/* snapshot */
.snap-bg{position:absolute;left:0;top:1257px;width:1200px;height:803px;background:var(--paper)}
.photo{position:absolute;border:3px solid #d7d9d9}
.meta{position:absolute;left:276px;top:1465px;font-size:16px;line-height:30px}
.quote{position:absolute;left:783px;top:1456px;width:365px;font-size:15px;font-style:italic;line-height:30px;color:#222}
.quote .who{position:absolute;right:8px;bottom:-4px;font-family:'Oswald',sans-serif;font-style:normal;font-weight:300;font-size:19px;color:var(--sky)}
.divider{position:absolute;left:80px;top:1627px;width:1056px;border-top:1px solid #e2e4e4}
.price{position:absolute;left:62px;top:1738px;font-family:'Oswald',sans-serif;font-weight:500;font-size:204px;line-height:1;color:var(--orange);letter-spacing:-4px}
.contest-copy{position:absolute;left:369px;top:1780px;width:540px;font-family:'Oswald',sans-serif;font-weight:300;font-size:17px;line-height:24px;color:var(--muted)}
.contest-copy b{font-weight:500;color:var(--teal)}
.start{left:365px;top:1923px;width:548px;height:89px;background:var(--teal);font-size:50px;line-height:89px}

/* latest */
.latest-bg{position:absolute;left:0;top:2060px;width:1200px;height:495px;background:var(--grey)}
.card{position:absolute;top:2240px;width:230px;height:244px;background:var(--ink);color:#fff;text-align:center}
.card .thumb{position:absolute;left:12px;top:12px;width:206px;height:128px}
.card h3{position:absolute;top:158px;width:100%;font-size:16px;font-weight:600}
.card p{position:absolute;top:190px;width:100%;font-size:15px;font-weight:600;color:#7a8b8e}
.card p b{color:var(--teal)}
.cta{top:2610px;width:453px;height:88px;font-size:50px;line-height:88px}

/* press */
.press{position:absolute;left:0;top:2750px;width:1200px;height:85px;background:#eef0f0;display:flex;align-items:center;justify-content:center;gap:32px;font-size:32px;color:#1d5d9b}
.press .c2{color:#e0243e;font-weight:300}
.press .c4{font-family:'Oswald',sans-serif;color:#111}
.press .c5{color:#1e88c6}

/* footer */
.site-footer{position:absolute;left:0;top:2835px;width:1200px;height:282px;background:var(--ink-2);color:#9aa8aa;font-size:12px}
.col{position:absolute;top:45px;width:180px}
.col h4{font-weight:400;font-size:12px;padding-bottom:18px;border-bottom:1px solid #2b4346;margin-bottom:26px}
.col li{list-style:none;line-height:26px}
.social{display:flex;gap:18px;margin-top:4px}
.social i{width:18px;height:18px;border-radius:50%;background:#fff;display:block}
.totals{position:absolute;left:0;top:3117px;width:1200px;height:111px;background:var(--band)}
.total{position:absolute;top:22px;width:300px;text-align:center;color:#fff;font-size:36px;font-weight:300;line-height:42px}
.total span{display:block;font-size:24px;color:#2e7f84}
.legal{position:absolute;left:0;top:3228px;width:1200px;height:251px;background:var(--ink);color:#8fa0a3;font-size:10.5px;line-height:18px}
.legal .blurb{position:absolute;left:72px;top:48px;width:1076px;text-align:center}
.legal .copy{position:absolute;left:72px;top:202px}
</style>
</head>
<body>

<header class="site-header">
  <div class="brand"><i></i>Gigwharf</div>
  <nav class="main-nav"><a>Homepage</a><a>Post Project</a><a>Find Freelancer</a><a>Browse projects</a><a>Post Contest</a></nav>
  <div class="login">Login</div>
  <div class="account">My Account</div>
  <div class="search">Search for Freelancers, Projects ...</div>
</header>

<section class="hero">
  <h1>Your <b>ideal design</b><br>only one click distance</h1>
  <p class="lead">Choose the type of work that you need done</p>
  <div class="sel">Category</div>
  <div class="hero-btn">Post Project</div>
  <hr>
  <p class="about">Gigwharf.com is the world's largest outsourcing marketplace, empowering entrepreneurs &amp; small businesses worldwide.</p>
  <div class="map" role="img" aria-label="Blue world map with connection lines"></div>
  <p class="count">OVER <b>7,364,543</b> PROFESSIONALS WORKING FOR YOU</p>
</section>

<h2 class="section-title how" style="top:640px">HOW IT WORKS ? <span>FIND OUT NOW !</span></h2>

<svg class="abs" style="left:0;top:1000px" width="1200" height="257" viewBox="0 1000 1200 257">
  <polygon points="0,1257 330,1205 760,1150 1080,1030 1200,1035 1200,1257" fill="#9dd6e4"/>
  <polygon points="60,1257 560,1235 900,1170 1200,1110 1200,1257" fill="#6fc3d6"/>
</svg>
<div class="steps-art" role="img" aria-label="Five numbered steps of how hiring works, arranged around a central mark"></div>
<div class="tooltip">Release<br>payment to the<br>freelancer</div>

<div class="video" role="img" aria-label="Explainer video player"><div class="bar"><i></i></div></div>
<div class="pill post-free">Post your project. <b>IT'S FREE!</b></div>
<p class="stat-line" style="left:963px;top:1158px">over <b>$1,115,768,146</b></p>
<p class="stat-line" style="left:709px;top:1207px">over <b>4,472,451</b> projects online</p>

<div class="snap-bg"></div>
<h2 class="section-title" style="top:1322px">PROJECT <span>SNAPSHOT</span></h2>
<div class="photo" role="img" aria-label="Interior design rendering" style="left:82px;top:1462px;width:154px;height:100px;background:linear-gradient(135deg,#8a8f93,#c9b08a)"></div>
<div class="meta"><b>Project:</b> Interior Design<br><b>Cost:</b> $200<br><b>Completed in:</b> 1 day</div>
<div class="photo" role="img" aria-label="Client portrait" style="left:643px;top:1454px;width:104px;height:104px;border:0;background:linear-gradient(#e8e8e8,#9a9a9a)"></div>
<p class="quote">“I posted a job to create an exact, photo-realistic computer generated rendering of my apartment. I included only a few simple sketches was amazed that i received over fifty bids” <span class="who">R. Halden</span></p>
<div class="divider"></div>

<h2 class="section-title" style="top:1660px">GIGWHARF <span>CONTEST</span></h2>
<div class="price">$30</div>
<p class="contest-copy">Every minute one project is posted on our website. Clients choose us for our low prices and high quality. You can try now.<br><br style="line-height:14px">From just <b>$30 USD</b>, get hundreds of entries and only pay for one you love!</p>
<div class="pill start">Start a contest</div>
<div class="abs" role="img" aria-label="White T-shirt with colourful origami birds" style="left:962px;top:1716px;width:228px;height:270px;border-radius:30px;background:linear-gradient(#fff,#eeeeee);border:1px solid #ddd"></div>

<div class="latest-bg"></div>
<div class="abs" role="img" aria-label="Flock of colourful origami birds" style="left:700px;top:2020px;width:460px;height:200px;border-radius:50%;background:radial-gradient(ellipse,rgba(240,137,42,.45),rgba(77,179,179,.35) 50%,rgba(220,221,221,0) 72%)"></div>
<h2 class="section-title" style="top:2120px">LATESTS <span>PROJECTS</span></h2>
<div class="card" style="left:100px"><div class="thumb" role="img" aria-label="Abstract 3D artwork" style="background:linear-gradient(135deg,#f2f2f2,#9aa3b0,#c23)"></div><h3>Project title Go Here</h3><p>Budget <b>$500</b></p></div>
<div class="card" style="left:375px"><div class="thumb" role="img" aria-label="Abstract blue sculpture" style="background:linear-gradient(135deg,#e6e7ea,#4a3f8f,#dcdde2)"></div><h3>Project title Go Here</h3><p>Budget <b>$500</b></p></div>
<div class="card" style="left:651px"><div class="thumb" role="img" aria-label="Colourful graffiti illustration" style="background:linear-gradient(135deg,#5a2e1b,#7bc34a,#d8a629)"></div><h3>Project title Go Here</h3><p>Budget <b>$500</b></p></div>
<div class="card" style="left:923px"><div class="thumb" role="img" aria-label="Vector heart with flowers" style="background:radial-gradient(circle,#ffd23b,#f07a10,#c5231a)"></div><h3>Project title Go Here</h3><p>Budget <b>$500</b></p></div>

<div class="pill cta" style="left:115px;background:var(--teal)">Start a contest</div>
<div class="pill cta" style="left:655px;background:var(--ink)">Post a project</div>

<div class="press">
  <span style="font-weight:700">Ledgerline</span><span class="c2">dailyonline</span><span>EPOCH</span><span class="c4">The Harbor Gazette</span><span class="c5">The Market Courier</span>
</div>

<footer class="site-footer">
  <div class="col" style="left:94px"><h4>Get in Touch</h4><ul><li>In The News</li><li>Press Releases</li><li>Awards</li><li>Testimonials</li></ul></div>
  <div class="col" style="left:357px"><h4>Get in Touch</h4><ul><li>About us</li><li>Competitions</li><li>Developer API</li></ul></div>
  <div class="col" style="left:624px"><h4>Get in Touch</h4><ul style="margin-top:-8px;line-height:29px"><li>Advertise with us</li><li>Careers</li><li>Gigwharf Blog</li><li>Affiliate Program</li><li>Affiliate API</li></ul></div>
  <div class="col" style="left:874px"><h4 style="border:0">Stay connected</h4><div class="social"><i></i><i></i><i></i><i></i><i></i></div></div>
</footer>

<div class="totals">
  <div class="total" style="left:92px">7,366,855<span>professionals</span></div>
  <div class="total" style="left:423px">$1,115,967,086<span>projects posted</span></div>
  <div class="total" style="left:754px">4,473,289<span>projects</span></div>
</div>

<div class="legal">
  <p class="blurb">Gigwharf.com (formerly GetAGigster, Codelance and taskHub/Hirecoder) is the world's largest freelancing, outsourcing and crowdsourcing marketplace for small business. Hire freelancers to work in software, writing, data entry and design right through to engineering and the sciences, sales and marketing, and accounting &amp; legal services. Find freelance jobs and make money online! We have freelance coders, writers, programmers, designers, marketers and more. Getting the best web design, custom programming, professional writing or affordable marketing has never been easier!</p>
  <p class="copy">© Copyright 2013 Gigwharf Technology Pty Limited (ACN 142 189 759)<br>Gigwharf ® is a registered Trademark of Gigwharf Technology Pty Limited (ACN 142 189 759)</p>
</div>

</body>
</html>
```